Billboard design for dentist that sees only children

I own a 12' x 25' digital billboard and I need help with billboard design. My wife is a general dentist that only sees children and is very passionate about giving them a quality dental experience . She has a great reputation in town. Obviously with a billboard there can't be a lot of reading. Maybe something that shows safety, love, experience and children. I am completely open to your ideas. In addition I have other businesses that also need billboard design so this could lead to more work. If you go to Maplecovedental.com under the about section you will find more information about the practice and our phone number. Attached is our logo which could be changed and content specs for the digital billboard. Happy Designing!!

Target Market(s)

Parents with children

Colors

Designer to choose colors to be used in the design.

Requirements
Must have
• Must attract attention and be nice to look at.
Nice to have
• Probably should have children in the picture ..... Maybe
Should not have
• If I see something I don't like I will let you know

```html
<!DOCTYPE html>
<html lang="en">
<head>
<meta charset="utf-8">
<title>Maple Cove Dental — Billboard</title>
<link rel="stylesheet" href="https://fonts.googleapis.com/css2?family=Alegreya+Sans:ital,wght@1,400;1,500&family=Arimo:wght@400&display=swap">
<style>
  :root {
    --page-bg: #f2f1ea;
    --paper: #ffffff;
    --brand-green: #1f8a6e;
    --brand-navy: #2a1f72;
    --deep-navy: #1c1566;
    --mid-blue: #2a63b4;
    --bright-blue: #0a9ade;
    --photo-warm: #e9c6b0;
    --photo-cool: #b9d6e6;
    --url-white: #ffffff;
  }
  * { margin: 0; padding: 0; box-sizing: border-box; }
  html, body {
    width: 1200px;
    height: 888px;
    overflow: hidden;
    background: var(--page-bg);
  }
  .billboard {
    position: absolute;
    left: 0;
    top: 154px;
    width: 1200px;
    height: 579px;
    display: block;
  }
  .headline {
    font-family: "Alegreya Sans", sans-serif;
    font-style: italic;
    font-weight: 500;
    fill: var(--brand-green);
  }
  .tagline {
    font-family: "Alegreya Sans", sans-serif;
    font-style: italic;
    font-weight: 400;
    fill: var(--brand-navy);
  }
  .brand-name {
    font-family: "Alegreya Sans", sans-serif;
    font-style: italic;
    font-weight: 500;
    fill: var(--brand-green);
  }
  .web-address {
    font-family: "Arimo", sans-serif;
    font-weight: 400;
    fill: var(--url-white);
  }
</style>
</head>
<body>
<svg class="billboard" viewBox="0 0 1140 550" xmlns="http://www.w3.org/2000/svg">
  <defs>
    <linearGradient id="band-gradient" x1="0" y1="0" x2="1" y2="0">
      <stop offset="0" stop-color="var(--deep-navy)"/>
      <stop offset="0.35" stop-color="var(--mid-blue)"/>
      <stop offset="0.7" stop-color="var(--bright-blue)"/>
      <stop offset="0.92" stop-color="var(--mid-blue)"/>
      <stop offset="1" stop-color="var(--deep-navy)"/>
    </linearGradient>
    <linearGradient id="photo-gradient" x1="0" y1="0" x2="1" y2="1">
      <stop offset="0" stop-color="var(--photo-warm)"/>
      <stop offset="0.6" stop-color="var(--photo-cool)"/>
      <stop offset="1" stop-color="#c7dcb0"/>
    </linearGradient>
  </defs>

  <rect class="panel" x="0" y="0" width="1140" height="550" fill="var(--paper)"/>
  <rect class="top-band" x="0" y="0" width="1140" height="22" fill="url(#band-gradient)"/>

  <rect class="children-photo" role="img" aria-label="Photo of four laughing children leaning in together" x="680" y="30" width="460" height="450" rx="40" fill="url(#photo-gradient)" opacity="0.85"/>

  <path class="green-swoosh" fill="var(--brand-green)"
        d="M0 400 C80 384 160 376 230 372 L440 392 C620 420 760 480 900 478 C990 476 1080 440 1140 420 L1140 470 C1060 488 980 494 900 494 C760 494 600 440 440 408 L230 404 C150 410 70 430 0 452 Z"/>
  <path class="blue-base" fill="url(#band-gradient)"
        d="M0 452 C70 430 150 410 230 404 L440 408 C600 440 760 494 900 494 C980 494 1060 488 1140 470 L1140 550 L0 550 Z"/>

  <text class="headline" x="18" y="172" font-size="74">Maple Cove Dental</text>
  <text class="tagline" x="666" y="210" font-size="35" text-anchor="end">general dentistry for children</text>

  <g class="brand-mark">
    <circle cx="238" cy="318" r="26" fill="var(--bright-blue)"/>
    <text class="brand-name" x="276" y="330" font-size="34">Maple Cove Dental</text>
  </g>

  <text class="web-address" x="112" y="515" font-size="38">www.maplecovedental.com</text>
</svg>
</body>
</html>
```